依頼詳細
今回作成するチラシは朝凪新報様へ折込む集客チラシの作成です。
しっかり集客ができる動線で作っていただきたいです。
「集客」という目標が最大限できれば、それ以外は求めません。
ターゲットは50代夫婦で子供は独立している方々です。お金は多少余裕があり、お庭の雑草対策に悩んでいる方へ最新技術の雑草の生えない人工芝をしっかりアピール(集客)したいです。
また、このチラシで集客するために、訪問見積もりご依頼いただいたお客様対象「限定15名 スパークリングワイン&スペシャルグラスプレゼント」キャンペーンをする予定です。
スパークリングワイン1本とスペシャルグラス2つプレゼントです。URLは以下の通りです。

https://www.kaimono-ichiba.example/[ルミオン]Lumion-フルートグラス-ステムレスグラスセット/dp/X00000001/

https://www.kaimono-ichiba.example/コルネット-厳選泡6本セット-750mlx6本ワインセット/dp/X00000002/
記載項目
社名:緑野芝生工房株式会社 / 電話:0120-555-318 / URL:tobu-lawn.example
サイズ
A4
ページ数
片面
希望イメージ
シンプル 複雑
単色 カラフル
暗い 明るい
日常 高級
遊び心 厳粛
未来的 伝統的
女性的 男性的
希望する色
緑系、集客さえできるチラシであれば何色を使っても正解です。
補足説明
必要な画像は弊社ホームページからいくらでも転用ください。
そのほか必要な画像は申しつけください。
追加でイメージをお伝えします。
新聞購読者が弊社折込チラシをパッと見て捨てないデザイン(インパクト・限定感・わかりやすさ)で、
電話番号大きくして「今すぐ電話しよう!」と自然とすぐ行動するような導線にしてください。
データを参考に添付します。
【仕様変更】

依頼内容の大幅な変更をお願いいたします。
キャンペーン「スパークリング ワイン・グラスプレゼント」は中止となりました。
もうすでにお取り組みされておられるランサーの方々には大変申し訳ございませんが、「スパークリングワイン・グラスプレゼント」は記載しないようお願いいたします。
また、その代わりにキャンペーン文言「もうすぐ完売! 【キャンペーンプラン】」というように訴求くださると助かります。(訴求のためでしたら追加で【急げ!】【期間限定!】等を追加で入れても問題ございません。)

「もうすぐ完売! 【キャンペーンプラン】」について補足いたします。
弊社では人工芝工事に「エコノミープラン」「ビジネスプラン」「ファーストクラスプラン」がありますが、
キャンペーンプランは通常の「ビジネスプラン」より約21,000円お安く工事が可能なプランです。
(上記のプランの説明を入れることは必須ということではございません。あくまでランサー様へご理解いただくため記載申し上げました。)
内容が大幅に変更となったこと、重ねてお詫び申し上げます。
■ 選んだ理由

訴求から問い合わせまでの動線と内容がよく、木になる人にも情報を提供していたため、デザインだけでなく、情報提供力に優れていたからです。

■ 提案者全員のお礼・コメント

ご提案くださりました全ての方々に、御礼申し上げます。
次回以降ももし可能でしたら優秀な皆様にまたご提案いただけますと嬉しい限りでございます。

```html
<!DOCTYPE html>
<html lang="ja">
<head>
<meta charset="utf-8">
<title>人工芝 集客チラシ</title>
<link href="https://fonts.googleapis.com/css2?family=Noto+Sans+JP:wght@500;700;900&family=Roboto+Condensed:wght@700&display=swap" rel="stylesheet">
<style>
  :root{
    --grass-dark:#2c5e1b;
    --grass-mid:#3f7d28;
    --grass-light:#5b9a38;
    --yellow:#f6e20c;
    --white:#ffffff;
    --ink:#111111;
    --campaign-green:#3c8a24;
    --frame-gold:#d9c66a;
  }
  *{box-sizing:border-box;margin:0;padding:0}
  html,body{width:848px;height:1200px;overflow:hidden}
  body{font-family:"Noto Sans JP",sans-serif;color:var(--white)}
  .flyer{position:relative;width:848px;height:1200px;overflow:hidden;
    background:radial-gradient(ellipse at 50% 40%,var(--grass-light) 0%,var(--grass-mid) 45%,var(--grass-dark) 100%)}
  .abs{position:absolute}

  .tagline{top:40px;left:0;width:100%;text-align:center;color:var(--yellow);font-weight:900;font-size:30px;letter-spacing:2px;text-shadow:0 2px 3px rgba(0,0,0,.5)}
  .headline{top:92px;left:0;width:100%;text-align:center;color:var(--yellow);font-weight:900;font-size:176px;line-height:1;letter-spacing:10px;
    -webkit-text-stroke:5px var(--ink);paint-order:stroke fill;text-shadow:0 6px 10px rgba(0,0,0,.45)}
  .intro{top:284px;left:190px;width:510px;text-align:right;font-size:15px;font-weight:700;line-height:1.72;white-space:nowrap;text-shadow:0 1px 2px rgba(0,0,0,.7)}
  .intro-photo{top:318px;left:712px;width:110px;height:80px;border-radius:4px;background:linear-gradient(160deg,#8dbf5a,#4f8a2c)}

  .chosen{top:420px;left:58px;background:var(--ink);color:var(--white);font-size:28px;font-weight:900;padding:3px 12px;letter-spacing:1px}
  .price{top:470px;left:58px;color:var(--white);font-weight:900;font-size:26px;white-space:nowrap}
  .price strong{color:var(--yellow);font-size:42px;font-family:"Roboto Condensed","Noto Sans JP",sans-serif}
  .price .unit{color:var(--yellow);font-size:22px}
  .uses{top:530px;left:58px;display:flex;gap:6px;list-style:none}
  .use{width:122px}
  .use-photo{height:70px;border:2px solid var(--white)}
  .use-photo.garden{background:linear-gradient(#9bb9c9,#5f9a3a)}
  .use-photo.terrace{background:linear-gradient(#c9c4b8,#6aa046)}
  .use-photo.parking{background:linear-gradient(#b7b1a6,#5d9339)}
  .use-caption{background:var(--white);color:var(--ink);font-size:11px;font-weight:700;text-align:center;padding:2px 0;white-space:nowrap}

  .house{top:415px;left:470px;width:345px;height:360px;background:linear-gradient(135deg,#8a8a8a 0%,#b9b2a6 45%,#7db356 100%);border-radius:4px}
  .ask{top:650px;left:58px;color:var(--yellow);font-weight:900;font-size:34px;text-shadow:0 2px 3px rgba(0,0,0,.5)}

  .guide{top:700px;left:404px}
  .brand{top:815px;left:0;width:100%;text-align:center}
  .brand-mark{display:inline-block;width:46px;height:46px;border:3px solid var(--frame-gold)}
  .brand-name{display:block;font-size:20px;font-weight:700;color:var(--white);letter-spacing:3px;margin-top:2px}

  .company{top:912px;left:224px;width:400px;border:2px solid var(--white);text-align:center;padding:4px 0 2px}
  .company-name{font-size:48px;font-weight:900;letter-spacing:4px;line-height:1.1}
  .company-en{font-size:10px;letter-spacing:3px;font-weight:500}
  .phone{top:1003px;left:218px;width:412px;display:flex;align-items:center;gap:8px;border-bottom:2px solid var(--white);padding-bottom:2px}
  .phone-number{font-family:"Roboto Condensed",sans-serif;font-size:56px;font-weight:700;letter-spacing:1px;line-height:1}
  .hours{top:1074px;left:0;width:100%;text-align:center;font-size:14px;font-weight:700}
  .url{top:1106px;left:0;width:100%;text-align:center;font-family:"Roboto Condensed",sans-serif;font-size:38px;font-weight:700}

  .award{left:18px;width:180px;height:96px}
  .award.quality{top:915px}
  .award.satisfaction{top:1030px}

  .hurry{top:880px;left:742px;width:90px;height:90px;border-radius:50%;background:var(--yellow);color:var(--ink);font-weight:900;font-size:16px;display:flex;align-items:center;justify-content:center;text-align:center;line-height:1.2}
  .campaign{top:978px;left:642px;width:194px;background:var(--campaign-green);border:2px solid var(--white);text-align:center;padding:6px 4px}
  .campaign-lead{font-size:14px;font-weight:900;color:var(--yellow)}
  .campaign-title{font-size:19px;font-weight:900;margin-bottom:4px}
  .campaign-note{background:var(--white);color:var(--campaign-green);font-size:11px;font-weight:700;padding:2px;margin:0 6px 4px}
  .campaign-sub{font-size:11px;font-weight:700;line-height:1.4}
  .discount{top:1104px;left:642px;width:194px;text-align:center;color:var(--yellow);font-weight:900;font-size:42px;line-height:1;font-family:"Roboto Condensed","Noto Sans JP",sans-serif;text-shadow:0 2px 3px rgba(0,0,0,.5)}
  .discount small{display:block;font-size:22px;color:var(--white);margin-top:2px}
</style>
</head>
<body>
<main class="flyer">
  <p class="abs tagline">雑草が生えない！ 10年快適!!</p>
  <h1 class="abs headline">人工芝</h1>

  <p class="abs intro">21世紀のご自宅は、より快適・より機能的な住まいの時代です<br>雑草が生えない、10年もつ強度はもちろん<br>最新技術の結晶であるフワフワ人工芝が<br>弊社の提供する21世紀の快適さです</p>
  <div class="abs intro-photo" role="img" aria-label="人工芝の上で寝転ぶ子どもの写真"></div>

  <p class="abs chosen">今、選ばれています</p>
  <p class="abs price"><strong>7,800</strong>円<span class="unit">/m²</span>～からの人工芝</p>
  <ul class="abs uses">
    <li class="use"><div class="use-photo garden" role="img" aria-label="人工芝を施工した庭の写真"></div><p class="use-caption">お庭を人工芝へ</p></li>
    <li class="use"><div class="use-photo terrace" role="img" aria-label="人工芝を敷いたマンションテラスの写真"></div><p class="use-caption">マンションテラス</p></li>
    <li class="use"><div class="use-photo parking" role="img" aria-label="駐車場のコンクリートを人工芝にした写真"></div><p class="use-caption">駐車場コンクリートへ</p></li>
  </ul>
  <div class="abs house" role="img" aria-label="人工芝の庭がある住宅の俯瞰イラスト"></div>

  <p class="abs ask">まずはお問い合わせ…</p>

  <svg class="abs guide" width="40" height="110" viewBox="0 0 40 110" aria-hidden="true">
    <line x1="20" y1="0" x2="20" y2="92" stroke="#ffffff" stroke-width="3" stroke-dasharray="6 6"/>
    <polyline points="8,88 20,104 32,88" fill="none" stroke="#ffffff" stroke-width="3"/>
  </svg>

  <div class="abs brand">
    <span class="brand-mark"></span>
    <span class="brand-name">ryokuya</span>
  </div>

  <div class="abs company">
    <p class="company-name">緑野芝生工房</p>
    <p class="company-en">RYOKUYA SHIBAFU KOUBOU CO., LTD.</p>
  </div>

  <div class="abs phone">
    <svg width="52" height="44" viewBox="0 0 52 44" aria-hidden="true">
      <rect x="1" y="1" width="50" height="42" rx="6" fill="#ffffff"/>
      <path d="M16 12c3-2 6 4 4 6l-2 2c2 4 5 7 9 9l2-2c2-2 8 1 6 4-2 4-6 5-10 3-7-3-12-8-14-15-1-3 2-6 5-7z" fill="#2c5e1b"/>
    </svg>
    <span class="phone-number">0120-555-318</span>
  </div>
  <p class="abs hours">【受付時間】平日 9:00～20:00</p>
  <p class="abs url">https://tobu-lawn.example</p>

  <div class="abs award quality" role="img" aria-label="人工芝施工品質 第1位獲得の受賞バッジ">
    <svg width="180" height="96" viewBox="0 0 180 96" aria-hidden="true"><ellipse cx="90" cy="48" rx="87" ry="44" fill="none" stroke="#d9c66a" stroke-width="3"/></svg>
  </div>
  <div class="abs award satisfaction" role="img" aria-label="お客様満足度 第1位獲得の受賞バッジ">
    <svg width="180" height="96" viewBox="0 0 180 96" aria-hidden="true"><ellipse cx="90" cy="48" rx="87" ry="44" fill="none" stroke="#d9c66a" stroke-width="3"/></svg>
  </div>

  <p class="abs hurry">お急ぎ<br>下さい!!</p>
  <div class="abs campaign">
    <p class="campaign-lead">もうすぐ完売</p>
    <p class="campaign-title">キャンペーンプラン</p>
    <p class="campaign-note">ビジネスプラン比較</p>
    <p class="campaign-sub">通常のビジネスプランより<br>工事費用がおトクに</p>
  </div>
  <p class="abs discount">21,000円<small>OFF</small></p>
</main>
</body>
</html>
```